Velmora and Co Business Card Design

Looking for a business card design. Wanting Smart, Clean and Sharp looking to promote Velmora and Co, our Import Export Business - like Black, White and natural textures. I have uploaded our logo. I like a rounded font but open to other ideas
Being that we have a wide range of products on offer we are looking for a neutral yet eye catching card. We would also like to have Import - Export on the business card to be clear on want our business does.

Target Market(s)

Import export market

Industry/Entity Type

Importer

Contact Information for Business Card

Mr Tobias Kernwell
tobias.kernwell@velmoraandco.com.au
+61 (0) 417 630 284
www.velmoraandco.com.au

Font styles to use
Other font styles liked:
• Unsure of actual font name but something rounded and clean

Colors

Designer to choose colors to be used in the design.

Requirements
Must have
• Instagram icon
• Facebook icon

```html
<!DOCTYPE html>
<html lang="en">
<head>
<meta charset="UTF-8">
<title>Velmora and Co — Business Card</title>
<link rel="stylesheet" href="https://fonts.googleapis.com/css2?family=Jost:wght@400;500;600&display=swap">
<style>
  :root {
    --backdrop: #2a2a2a;
    --card-black: #1b1b1b;
    --card-white: #ffffff;
    --ink: #1a1a1a;
    --ink-soft: #2e2e2e;
    --paper-text: #ffffff;
  }
  * { margin: 0; padding: 0; box-sizing: border-box; }
  html, body {
    width: 1200px; height: 895px; overflow: hidden;
    background: var(--backdrop);
    font-family: "Jost", "Futura", sans-serif;
  }
  .stage {
    width: 1200px; height: 895px;
    display: flex; flex-direction: column; align-items: center; justify-content: center;
    gap: 36px;
  }
  .card {
    position: relative;
    width: 700px; height: 400px;
    box-shadow: 0 10px 30px rgba(0,0,0,0.45);
  }
  .card--front { background: var(--card-black); color: var(--paper-text); }
  .card--back { background: var(--card-white); color: var(--ink); }

  .brand {
    position: absolute; left: 245px; top: 62px;
    width: 210px;
    display: flex; flex-direction: column; align-items: center;
  }
  .brand__block {
    width: 210px; height: 210px;
    background: var(--paper-text);
    display: flex; align-items: center; justify-content: center;
  }
  .brand__name {
    color: var(--card-black);
    font-size: 32px; font-weight: 600; letter-spacing: 1px; text-transform: uppercase;
    line-height: 1.05; text-align: center;
  }
  .brand__tagline {
    margin-top: 18px;
    font-size: 14px; font-weight: 500; letter-spacing: 1.5px;
  }
  .social {
    position: absolute; right: 62px; top: 150px;
    display: flex; gap: 10px;
  }
  .social__tile { width: 22px; height: 22px; background: var(--paper-text); }

  .holder {
    position: absolute; right: 395px; top: 232px;
    text-align: right;
  }
  .holder__name { font-size: 22px; font-weight: 600; letter-spacing: 0.5px; text-transform: uppercase; white-space: nowrap; }
  .holder__role { font-size: 16px; font-weight: 400; color: var(--ink-soft); margin-top: 2px; }
  .divider {
    position: absolute; left: 330px; top: 178px;
    width: 1.5px; height: 110px; background: var(--ink);
  }
  .contacts {
    position: absolute; left: 352px; top: 186px;
    list-style: none;
    display: flex; flex-direction: column; gap: 9px;
    font-size: 14.5px; color: var(--ink-soft);
  }
  .contacts__item { display: flex; align-items: center; gap: 10px; white-space: nowrap; }
  .contacts__icon { width: 14px; height: 14px; flex: none; }
</style>
</head>
<body>
<main class="stage">
  <section class="card card--front" aria-label="Card front">
    <div class="brand">
      <div class="brand__block">
        <span class="brand__name">Velmora<br>and Co</span>
      </div>
      <p class="brand__tagline">Import and Export</p>
    </div>
    <div class="social" aria-label="Social profiles">
      <span class="social__tile" role="img" aria-label="Social profile one"></span>
      <span class="social__tile" role="img" aria-label="Social profile two"></span>
    </div>
  </section>

  <section class="card card--back" aria-label="Card back">
    <div class="holder">
      <p class="holder__name">Mr Tobias Kernwell</p>
      <p class="holder__role">Founder &amp; CEO</p>
    </div>
    <span class="divider" aria-hidden="true"></span>
    <ul class="contacts">
      <li class="contacts__item">
        <svg class="contacts__icon" viewBox="0 0 24 24" aria-hidden="true"><path fill="#1a1a1a" d="M6.6 10.8a15.5 15.5 0 0 0 6.6 6.6l2.2-2.2c.3-.3.7-.4 1-.2 1.1.4 2.3.6 3.6.6.6 0 1 .4 1 1V20c0 .6-.4 1-1 1A17 17 0 0 1 3 4c0-.6.4-1 1-1h3.5c.6 0 1 .4 1 1 0 1.3.2 2.5.6 3.6.1.3 0 .7-.2 1z"/></svg>
        <span>+61 (0) 417 630 284</span>
      </li>
      <li class="contacts__item">
        <svg class="contacts__icon" viewBox="0 0 24 24" aria-hidden="true"><path fill="#1a1a1a" d="M2 5h20v14H2z"/><path fill="none" stroke="#fff" stroke-width="1.6" d="M2.5 5.5 12 13l9.5-7.5"/></svg>
        <span>tobias.kernwell@velmoraandco.com.au</span>
      </li>
      <li class="contacts__item">
        <svg class="contacts__icon" viewBox="0 0 24 24" aria-hidden="true"><circle cx="12" cy="12" r="10" fill="#1a1a1a"/><g fill="none" stroke="#fff" stroke-width="1.3"><ellipse cx="12" cy="12" rx="4.5" ry="10"/><path d="M2 12h20M4 7h16M4 17h16"/></g></svg>
        <span>www.velmoraandco.com.au</span>
      </li>
    </ul>
  </section>
</main>
</body>
</html>
```